K & D A/C Compressors' Business Card

Hello,

I need someone to create a new business card for my business. The name of my Business is: K & D A/C Compressors. I sell automotive air conditioning parts (a/c parts). I would like the business card to incorporate my logo, and to have an automotive feel to it. It is important that the business card feel like it is coming from an automotive parts business.

I already have a logo, which I will provide.

Thanks.

Project Deadline Extended Reason: I feel like extending the deadline until October 9, 2017, will allow for more time to design the business card. Thank you for your understanding. Added Monday, October 2, 2017

Target Market(s)

Consumers who need automotive a/c parts, and auto mechanics.

Industry/Entity Type

Automotive

Contact Information for Business Card

Business name: K & D A/C Compressors
Business Address: 48207 Southwest 64th Avenue, North Miami Beach, Florida 33847
Telephone: 305-642-1730
Fax: To be provided once I choose your design.
Website: www.kdcoolparts.example
Email: support@kdcoolparts.example
Names: To be provided once I choose your design.

Font styles to use
Sans Serif

Colors

Designer to choose colors to be used in the design.

Requirements
Must have
• The business card must include all of the "Business Card Details" and the logo I have uploaded.

```html
<!DOCTYPE html>
<html lang="en">
<head>
<meta charset="utf-8">
<title>K &amp; D A/C Compressors – Business Card</title>
<link rel="stylesheet" href="https://fonts.googleapis.com/css2?family=Open+Sans:wght@400;600;700&display=swap">
<style>
  :root {
    --page-bg: #e8e8ea;
    --card-blue: #00adee;
    --card-grey: #a7a9ac;
    --card-white: #ffffff;
    --text-light: #ffffff;
    --brand-grey: #9d9fa2;
    --shadow: rgba(0, 0, 0, 0.18);
  }
  * { margin: 0; padding: 0; box-sizing: border-box; }
  html, body {
    width: 1200px;
    height: 900px;
    overflow: hidden;
    background: var(--page-bg);
    font-family: "Open Sans", Arial, sans-serif;
  }
  .canvas { position: relative; width: 1200px; height: 900px; }

  .card {
    position: absolute;
    overflow: hidden;
    box-shadow: 0 6px 18px var(--shadow);
  }

  /* Front side */
  .card-front {
    left: 78px; top: 34px;
    width: 588px; height: 364px;
    background: var(--card-blue);
    color: var(--text-light);
  }
  .card-front .split-band {
    position: absolute; inset: 0;
    width: 100%; height: 100%;
  }
  .card-front .split-band polygon { fill: var(--card-grey); }

  .holder { position: absolute; left: 29px; top: 40px; }
  .holder-name {
    font-size: 20px; font-weight: 700; letter-spacing: 0.2px; line-height: 26px;
  }
  .holder-title { font-size: 15px; font-weight: 400; line-height: 18px; }

  .address {
    position: absolute; left: 26px; top: 177px;
    font-size: 15px; line-height: 22px; font-style: normal;
  }

  .contacts {
    position: absolute; left: 29px; top: 242px;
    list-style: none; font-size: 15px; line-height: 22px;
  }
  .contacts li { display: flex; align-items: center; gap: 7px; }
  .contacts svg { width: 12px; height: 12px; fill: var(--text-light); flex: none; }

  /* Back side */
  .card-back {
    left: 388px; top: 505px;
    width: 567px; height: 352px;
    background: var(--card-white);
  }
  .brand {
    position: absolute; left: 0; right: 0; top: 128px;
    display: flex; align-items: center; justify-content: center; gap: 14px;
    color: var(--brand-grey);
  }
  .brand-square { width: 40px; height: 40px; background: var(--card-blue); }
  .brand-name {
    font-size: 27px; font-weight: 600; line-height: 34px; letter-spacing: 0.5px;
  }
</style>
</head>
<body>
<main class="canvas">

  <section class="card card-front" aria-label="Business card front">
    <svg class="split-band" viewBox="0 0 588 364" preserveAspectRatio="none" aria-hidden="true">
      <polygon points="588,0 588,364 235,364"/>
    </svg>

    <div class="holder">
      <p class="holder-name">MARCUS DELGADO</p>
      <p class="holder-title">Managing Director</p>
    </div>

    <address class="address">
      48207 Southwest 64th Avenue,<br>
      North Miami Beach, Florida 33847
    </address>

    <ul class="contacts">
      <li>
        <svg viewBox="0 0 12 12" aria-hidden="true"><path d="M2.4 0.6 4.3 2.9 3.3 4.3c.7 1.6 2.1 3 3.8 3.8l1.4-1 2.3 1.9-.9 2.1C5 11 .9 6.9 .4 1.5Z"/></svg>
        305-642-1730
      </li>
      <li>
        <svg viewBox="0 0 12 12" aria-hidden="true"><path d="M3 0h5l1 1v3h1.5L12 5.5V11H0V5.5L1.5 4H3Zm1 1v3h4V1.5ZM2 6v1h2V6Zm0 2v1h2V8Zm4-2v1h4V6Z"/></svg>
        305-642-1730
      </li>
      <li>
        <svg viewBox="0 0 12 12" aria-hidden="true"><circle cx="6" cy="6" r="6"/><path d="M1 6h10M6 1c-2 2.8-2 7.2 0 10M6 1c2 2.8 2 7.2 0 10" stroke="#00adee" stroke-width="0.9" fill="none"/></svg>
        www.kdcoolparts.example
      </li>
      <li>
        <svg viewBox="0 0 12 12" aria-hidden="true"><path d="M0 2h12v1L6 7 0 3Zm0 2.4 6 4 6-4V10H0Z"/></svg>
        support@kdcoolparts.example
      </li>
    </ul>
  </section>

  <section class="card card-back" aria-label="Business card back">
    <div class="brand">
      <span class="brand-square" aria-hidden="true"></span>
      <p class="brand-name">K &amp; D A/C Compressors</p>
    </div>
  </section>

</main>
</body>
</html>
```